브랜드 소개
다온먹거리나눔진흥원는 『농수산식품산업 진흥을 통해 국민의 안정적인 먹거리 확보와 삶의질 향상에 기여』를 목표로 설립되어 유통개선·수급안정·수출진흥·식품산업육성 등의 사업을 수행하고 있습니다. 홈페이지는 공사 홍보 및 각종 공고 안내, 공사의 다양한 지원사업에 대한 창구 역할을 하고 있습니다. 다온먹거리나눔진흥원의 타겟은 농어업인과 소비자입니다.

```html
<!DOCTYPE html>
<html lang="ko">
<head>
<meta charset="utf-8">
<title>다온먹거리나눔진흥원</title>
<link rel="stylesheet" href="https://fonts.googleapis.com/css2?family=Noto+Sans+KR:wght@300;400;500;700&display=swap">
<style>
  :root {
    --page-bg: #e9e8e5;
    --topbar: #2b2a28;
    --topbar-text: #c9c7c2;
    --nav-bg: #ffffff;
    --nav-text: #333333;
    --brand-green: #3f8f3a;
    --hero-dark: #1f2416;
    --hero-green: #6f8f3c;
    --hero-moss: #9fb25a;
    --soil: #2a211a;
    --white: #ffffff;
    --dot-off: rgba(255,255,255,0.45);
  }
  * { box-sizing: border-box; margin: 0; padding: 0; }
  html, body { width: 1200px; height: 1198px; overflow: hidden; }
  body {
    background: var(--page-bg);
    font-family: "Noto Sans KR", sans-serif;
    display: flex;
    align-items: center;
    justify-content: center;
  }
  .site { width: 1200px; height: 700px; background: var(--nav-bg); overflow: hidden; }

  .utility-bar {
    height: 32px; background: var(--topbar);
    display: flex; align-items: center; justify-content: space-between;
    padding: 0 128px; color: var(--topbar-text); font-size: 12px;
  }
  .lang-select {
    width: 120px; height: 20px; border: 1px solid #4a4845; background: #353431;
    display: flex; align-items: center; justify-content: space-between; padding: 0 8px;
  }
  .lang-select svg { width: 8px; height: 6px; }
  .utility-links { display: flex; align-items: center; gap: 22px; }
  .search-box {
    width: 170px; height: 20px; background: #3b3a37; border: 1px solid #4a4845;
    display: flex; align-items: center; justify-content: space-between; padding: 0 8px;
    font-size: 11px; color: #8d8a85;
  }
  .search-box svg { width: 12px; height: 12px; }

  .main-nav {
    height: 72px; display: flex; align-items: center; justify-content: space-between;
    padding: 0 128px; border-bottom: 1px solid #e2e2e2;
  }
  .brand { display: flex; align-items: center; gap: 10px; }
  .brand-mark { width: 22px; height: 22px; border-radius: 50%; background: var(--brand-green); }
  .brand-text { display: flex; flex-direction: column; }
  .brand-name { font-size: 17px; font-weight: 700; color: var(--brand-green); line-height: 1.2; }
  .brand-sub { font-size: 9px; font-weight: 700; color: var(--brand-green); letter-spacing: 0.2px; }
  .menu { display: flex; gap: 48px; list-style: none; font-size: 16px; font-weight: 500; color: var(--nav-text); }

  .hero { position: relative; height: 596px; }
  .hero-photo {
    position: absolute; inset: 0;
    background:
      linear-gradient(180deg, rgba(0,0,0,0) 72%, var(--soil) 88%, #1b1510 100%),
      radial-gradient(ellipse at 85% 25%, #c9a98a 0%, rgba(201,169,138,0) 22%),
      radial-gradient(ellipse at 30% 55%, var(--hero-moss) 0%, rgba(159,178,90,0) 45%),
      linear-gradient(90deg, var(--hero-dark) 0%, var(--hero-green) 45%, #5d7431 75%, var(--hero-dark) 100%);
  }
  .hero-shade { position: absolute; inset: 0; background: rgba(20,25,10,0.28); }
  .hero-copy {
    position: absolute; top: 120px; left: 0; right: 0; text-align: center;
    color: var(--white); line-height: 1.4;
  }
  .hero-copy .line-light { font-size: 40px; font-weight: 300; display: block; padding-right: 20px; }
  .hero-copy .line-bold { font-size: 44px; font-weight: 700; display: block; padding-right: 20px; }

  .services {
    position: absolute; top: 278px; left: 0; right: 0;
    display: flex; justify-content: center; gap: 48px; list-style: none; padding-right: 20px;
  }
  .service { width: 106px; text-align: center; color: var(--white); font-size: 14px; }
  .service-icon {
    width: 106px; height: 106px; border-radius: 50%;
    border: 2px solid rgba(255,255,255,0.85); background: rgba(255,255,255,0.08);
    display: flex; align-items: center; justify-content: center; margin-bottom: 14px;
  }
  .service-icon svg { width: 46px; height: 46px; fill: none; stroke: var(--white); stroke-width: 2; }

  .pager { position: absolute; bottom: 86px; left: 0; right: 0; display: flex; justify-content: center; gap: 8px; }
  .pager span { width: 9px; height: 9px; border-radius: 50%; background: var(--dot-off); }
  .pager span.active { background: var(--white); }
</style>
</head>
<body>
<div class="site">
  <div class="utility-bar">
    <div class="lang-select">English
      <svg viewBox="0 0 8 6"><path d="M0 0h8L4 6z" fill="#c9c7c2"/></svg>
    </div>
    <div class="utility-links">
      <span>로그인</span>
      <span>회원가입</span>
      <div class="search-box">검색어를 입력해주세요
        <svg viewBox="0 0 12 12"><circle cx="5" cy="5" r="3.8" fill="none" stroke="#e0ded9" stroke-width="1.6"/><path d="M8 8l3 3" stroke="#e0ded9" stroke-width="1.6"/></svg>
      </div>
    </div>
  </div>

  <nav class="main-nav">
    <div class="brand">
      <span class="brand-mark"></span>
      <div class="brand-text">
        <span class="brand-name">다온먹거리나눔진흥원</span>
        <span class="brand-sub">Daon Food Sharing Promotion Institute</span>
      </div>
    </div>
    <ul class="menu">
      <li>정보공개</li>
      <li>진흥원소개</li>
      <li>진흥원사업</li>
      <li>경영공시</li>
      <li>고객센터</li>
      <li>홍보센터</li>
    </ul>
  </nav>

  <section class="hero">
    <div class="hero-photo" role="img" aria-label="흙에서 돋아나는 새싹 위로 손이 물방울을 떨어뜨리는 사진"></div>
    <div class="hero-shade"></div>
    <h1 class="hero-copy">
      <span class="line-light">대한민국 농수산식품의</span>
      <span class="line-bold">행복한 변화가 시작됩니다</span>
    </h1>
    <ul class="services">
      <li class="service">
        <div class="service-icon"><svg viewBox="0 0 46 46"><circle cx="23" cy="23" r="6"/><circle cx="8" cy="10" r="3"/><circle cx="38" cy="10" r="3"/><circle cx="8" cy="36" r="3"/><circle cx="38" cy="36" r="3"/><path d="M10.5 12l8 7M35.5 12l-8 7M10.5 34l8-7M35.5 34l-8-7"/></svg></div>
        유통개선
      </li>
      <li class="service">
        <div class="service-icon"><svg viewBox="0 0 46 46"><path d="M12 24a8 8 0 0 1 3-15 10 10 0 0 1 18 3 7 7 0 0 1 1 13H12z"/><path d="M23 28v12M15 40h16M17 32h12"/></svg></div>
        수급안정
      </li>
      <li class="service">
        <div class="service-icon"><svg viewBox="0 0 46 46"><rect x="8" y="20" width="30" height="20"/><path d="M8 20l15-8 15 8M23 6v14M18 11l5-5 5 5"/></svg></div>
        수출진흥
      </li>
      <li class="service">
        <div class="service-icon"><svg viewBox="0 0 46 46"><path d="M6 40h34"/><rect x="9" y="28" width="6" height="12"/><rect x="20" y="22" width="6" height="18"/><rect x="31" y="16" width="6" height="24"/><path d="M8 20l10-7 8 4 12-10M33 7h5v5"/></svg></div>
        식품산업육성
      </li>
    </ul>
    <div class="pager"><span class="active"></span><span></span><span></span></div>
  </section>
</div>
</body>
</html>
```